4 Header designs for dating sites

I need 4 difrant / unique headers for 2 adult dating sites, 1 non adult dating site and a cheat with an other wife/men site.

The headers need to be 840x140px
Colors are up to you. make it good looking.

The project price is for 4 unique headers.

the domains are:

Kowrimalo.nl (kowrimalo)
Brenufalowinta.nl (brenufalowinta)
Plivornek.nl (plivornek)
Fudrakiso.nl (a dutch word for cheating)

Industry/Entity Type

Dating

Logo Text

use the domainnames

```html
<!DOCTYPE html>
<html lang="nl">
<head>
<meta charset="utf-8">
<title>Header designs – dating sites</title>
<link rel="stylesheet" href="https://fonts.googleapis.com/css2?family=Nunito+Sans:wght@400&display=swap">
<style>
  :root {
    --backdrop: #8c7762;
    --name-white: #ffffff;
    --magenta: #c4155a;
    --crimson: #d9263e;
    --berry: #8e1045;
    --plum: #5e1640;
    --wine: #7a0f33;
    --rose: #e0356a;
  }

  * { box-sizing: border-box; margin: 0; padding: 0; }

  html, body {
    width: 1200px;
    height: 1009px;
    overflow: hidden;
  }

  body {
    background: var(--backdrop);
    position: relative;
    font-family: "Nunito Sans", "Avenir Next", sans-serif;
  }

  .header-banner {
    position: absolute;
    left: 71px;
    width: 1029px;
    height: 171px;
    overflow: hidden;
  }

  .header-banner--brenufalowinta { top: 69px; }
  .header-banner--plivornek      { top: 273px; }
  .header-banner--fudrakiso      { top: 502px; }
  .header-banner--kowrimalo      { top: 720px; width: 1037px; }

  .banner-art {
    position: absolute;
    inset: 0;
  }

  .header-banner--brenufalowinta .banner-art {
    background:
      radial-gradient(ellipse at 72% 20%, var(--plum) 0%, transparent 45%),
      radial-gradient(ellipse at 20% 90%, var(--wine) 0%, transparent 50%),
      linear-gradient(100deg, var(--magenta) 0%, var(--rose) 35%, var(--crimson) 70%, var(--magenta) 100%);
  }

  .header-banner--plivornek .banner-art {
    background:
      radial-gradient(ellipse at 45% 85%, var(--wine) 0%, transparent 40%),
      radial-gradient(ellipse at 92% 70%, var(--plum) 0%, transparent 35%),
      linear-gradient(95deg, var(--magenta) 0%, var(--rose) 30%, var(--magenta) 65%, var(--berry) 100%);
  }

  .header-banner--fudrakiso .banner-art {
    background:
      radial-gradient(ellipse at 12% 10%, var(--crimson) 0%, transparent 40%),
      radial-gradient(ellipse at 75% 40%, var(--plum) 0%, transparent 45%),
      linear-gradient(100deg, var(--wine) 0%, var(--crimson) 35%, var(--berry) 65%, var(--plum) 100%);
  }

  .header-banner--kowrimalo .banner-art {
    background:
      radial-gradient(ellipse at 55% 30%, var(--plum) 0%, transparent 45%),
      radial-gradient(ellipse at 90% 80%, var(--magenta) 0%, transparent 35%),
      linear-gradient(100deg, var(--berry) 0%, var(--wine) 40%, var(--berry) 75%, var(--plum) 100%);
  }

  .banner-name {
    position: absolute;
    left: 32px;
    top: 50%;
    transform: translateY(-50%);
    color: var(--name-white);
    font-weight: 400;
    line-height: 1;
    white-space: nowrap;
    text-transform: uppercase;
    letter-spacing: 0.01em;
  }

  .header-banner--brenufalowinta .banner-name { font-size: 64px; left: 34px; }
  .header-banner--plivornek .banner-name,
  .header-banner--fudrakiso .banner-name,
  .header-banner--kowrimalo .banner-name { font-size: 104px; }
</style>
</head>
<body>
  <section class="header-banner header-banner--brenufalowinta">
    <div class="banner-art" role="img" aria-label="Low-poly faceted pattern in magenta, red and plum"></div>
    <h1 class="banner-name">Brenufalowinta.nl</h1>
  </section>

  <section class="header-banner header-banner--plivornek">
    <div class="banner-art" role="img" aria-label="Low-poly faceted pattern in pink and magenta"></div>
    <h1 class="banner-name">Plivornek.nl</h1>
  </section>

  <section class="header-banner header-banner--fudrakiso">
    <div class="banner-art" role="img" aria-label="Low-poly faceted pattern in red, wine and plum"></div>
    <h1 class="banner-name">Fudrakiso.nl</h1>
  </section>

  <section class="header-banner header-banner--kowrimalo">
    <div class="banner-art" role="img" aria-label="Low-poly faceted pattern in deep berry and wine"></div>
    <h1 class="banner-name">Kowrimalo.nl</h1>
  </section>
</body>
</html>
```